Thistleby's Organic's. I make and sell organic bath & body products. Nourishing bath & body products. Products are soaps, scrubs, lip balms, bath salts, baby & mother products (belly balm, nipple balm, diaper balm, baby bath soak, chest rub,) . I use botanical and or herbs in all my recipes. I create my own recipes. I like muted colors...but I would like something that will get your attention. I like the colors green and brown, but open to any other colors. I would also like to get information about labels (different sizes for my products) I do like the pasley print and maybe even a cute owl.

Target Market(s)

women, pregnant and nursing women, women with children and men

Industry/Entity Type

Baby

Contact Information for Business Card

Rhoda Quillmore
527-614-2870,rquillmore@lumaweb.net
rquillmore@lumaweb.net

Font styles to use
Other font styles liked:
• bree

Requirements
Must have
• Thistleby's Organic's, nourishing bath & body products. It needs to get a person attention. I would like to see cards that are hip and fun. I would also like to view cards that are classy. I do like muted colors but I do have an open mind (use any color you think would be right) So far a lot of the cards have had leaves....I really do not like that design.
Nice to have
• ???pasley in the background ?cute owl
Should not have
• leaves

```html
<!DOCTYPE html>
<html lang="en">
<head>
<meta charset="utf-8">
<title>Thistleby's Organic's — Business Card</title>
<link href="https://fonts.googleapis.com/css2?family=Arimo:wght@400;700&family=Dancing+Script:wght@700&display=swap" rel="stylesheet">
<style>
  :root {
    --green-deep: #3fa64a;
    --green-mid: #5db642;
    --green-light: #9fd04c;
    --soil: #461f19;
    --cream: #ffffff;
    --accent-veil: rgba(255, 255, 255, 0.16);
  }
  * { margin: 0; padding: 0; box-sizing: border-box; }
  html, body {
    width: 1200px;
    height: 704px;
    overflow: hidden;
    background: #ffffff;
  }
  .card {
    position: relative;
    width: 1200px;
    height: 704px;
    overflow: hidden;
    background: linear-gradient(135deg, var(--green-deep) 0%, var(--green-mid) 55%, var(--green-light) 100%);
  }
  .soil-band {
    position: absolute;
    left: 0;
    top: 469px;
    width: 1200px;
    height: 235px;
    background: var(--soil);
  }
  .flourish-area {
    position: absolute;
    left: 520px;
    top: 0;
    width: 680px;
    height: 704px;
    background: radial-gradient(ellipse at 70% 40%, var(--accent-veil) 0%, rgba(255,255,255,0.08) 45%, rgba(255,255,255,0) 75%);
  }
  .brand-name {
    position: absolute;
    left: 64px;
    top: 48px;
    font-family: "Arimo", Arial, sans-serif;
    font-weight: 700;
    font-size: 96px;
    line-height: 112px;
    color: var(--cream);
  }
  .brand-name span { display: block; }
  .contact-name {
    position: absolute;
    left: 64px;
    top: 522px;
    font-family: "Dancing Script", cursive;
    font-weight: 700;
    font-size: 56px;
    line-height: 64px;
    color: var(--cream);
  }
  .contact-details {
    position: absolute;
    left: 64px;
    top: 604px;
    font-family: "Arimo", Arial, sans-serif;
    font-weight: 400;
    font-size: 32px;
    line-height: 40px;
    color: var(--cream);
    white-space: nowrap;
  }
  .contact-details .divider { padding: 0 14px; }
</style>
</head>
<body>
  <div class="card">
    <div class="soil-band"></div>
    <div class="flourish-area" role="img" aria-label="Large faint pale-green botanical flourish sweeping across the right side"></div>
    <h1 class="brand-name">
      <span>Thistleby's</span>
      <span>Organic's</span>
    </h1>
    <p class="contact-name">Rhoda Quillmore</p>
    <p class="contact-details">Ph.: 527-614-2870<span class="divider">|</span>E-mail: rquillmore@lumaweb.net</p>
  </div>
</body>
</html>
```